Poster for Office

Looking for an edgy, beautiful poster to hang up in my office that uses the quotes located below and potentially the image attached.

Title: Hadley's Maxims

Must have the following quotes included (punctuation and capitalization are flexible, do what you think looks the best they also don't need the quotation symbols):

"Don't order fish at a steakhouse"
"Be bold. The more you tell, the more you sell"
"admit nothing, deny everything, launch counterattack."
"avoid obviousness"
"never do anything until you're ready to do it"
"look good=feel good"
"always keep the advantage"
"never complain, never explain"
"Lay low, play dumb, keep moving"

Quotes

• Title: Hadley's Maxims

"avoid obviousness"
"look good=feel good"

```html
<!DOCTYPE html>
<html lang="en">
<head>
<meta charset="utf-8">
<title>Hadley's Maxims</title>
<link rel="stylesheet" href="https://fonts.googleapis.com/css2?family=Special+Elite&display=swap">
<style>
  :root {
    --paper: #e4e4e4;
    --frame: #2a2a2a;
    --ink: #0a0a0a;
    --signal: #ff3b1c;
    --tone-light: #e0e0e0;
    --tone-mid: #a8a8a8;
    --tone-dark: #4a4a4a;
  }
  * { margin: 0; padding: 0; box-sizing: border-box; }
  html, body { width: 848px; height: 1200px; overflow: hidden; background: var(--paper); }
  .poster {
    position: relative;
    width: 848px;
    height: 1200px;
    background: var(--paper);
    border: 1.5px solid var(--frame);
    overflow: hidden;
    font-family: "Special Elite", "Courier New", monospace;
    text-transform: uppercase;
  }
  .photo-area {
    position: absolute;
    inset: 0;
    width: 848px;
    height: 1200px;
  }
  .title-plate {
    position: absolute;
    left: 56px; top: 141px;
    width: 594px; height: 94px;
    background: var(--signal);
    display: flex; align-items: center; justify-content: center;
  }
  .title-plate h1 {
    font-weight: 400;
    font-size: 46px;
    letter-spacing: 0.16em;
    color: var(--ink);
    white-space: nowrap;
    line-height: 1;
    padding-left: 0.16em;
  }
  .maxim {
    position: absolute;
    background: var(--ink);
    color: var(--signal);
    display: flex; align-items: center; justify-content: center;
    letter-spacing: 0.2em;
    white-space: nowrap;
    line-height: 1;
    overflow: hidden;
  }
  .maxim--look      { left: 135px; top: 503px; width: 543px; height: 32px; font-size: 23px; }
  .maxim--fish      { left: 85px;  top: 559px; width: 694px; height: 24px; font-size: 19px; }
  .maxim--bold      { left: 256px; top: 596px; width: 493px; height: 47px; font-size: 40px; justify-content: flex-start; padding-left: 26px; }
  .maxim--sell      { left: 85px;  top: 666px; width: 705px; height: 26px; font-size: 19px; }
  .maxim--admit     { left: 19px;  top: 718px; width: 818px; height: 24px; font-size: 15px; letter-spacing: 0.15em; }
  .maxim--obvious   { left: 182px; top: 765px; width: 465px; height: 35px; font-size: 26px; }
  .maxim--ready     { left: 5px;   top: 825px; width: 838px; height: 25px; font-size: 17px; letter-spacing: 0.16em; }
  .maxim--advantage { left: 21px;  top: 867px; width: 827px; height: 42px; font-size: 33px; }
  .maxim--low       { left: 106px; top: 930px; width: 625px; height: 24px; font-size: 18px; }
  .maxim--complain  { left: 37px;  top: 975px; width: 753px; height: 45px; font-size: 28px; }
</style>
</head>
<body>
<main class="poster">
  <svg class="photo-area" viewBox="0 0 848 1200" role="img" aria-label="Black and white photograph of a man seen from behind, bare shoulders and back filling the poster">
    <defs>
      <radialGradient id="photoTone" cx="0.5" cy="0.42" r="0.75">
        <stop offset="0" stop-color="var(--tone-light)"/>
        <stop offset="0.6" stop-color="var(--tone-mid)"/>
        <stop offset="1" stop-color="var(--tone-dark)"/>
      </radialGradient>
    </defs>
    <rect x="0" y="0" width="848" height="1200" fill="url(#photoTone)"/>
  </svg>

  <header class="title-plate">
    <h1>Hadley's Maxims</h1>
  </header>

  <p class="maxim maxim--look">Look good, feel good.</p>
  <p class="maxim maxim--fish">Don't order fish at a steakhouse.</p>
  <p class="maxim maxim--bold">Be bold.</p>
  <p class="maxim maxim--sell">The more you tell, the more you sell.</p>
  <p class="maxim maxim--admit">Admit nothing, deny everything, launch counterattack.</p>
  <p class="maxim maxim--obvious">Avoid obviousness.</p>
  <p class="maxim maxim--ready">Never do anything until you're ready to do it</p>
  <p class="maxim maxim--advantage">Always keep the advantage.</p>
  <p class="maxim maxim--low">Lay low, play dumb, keep moving.</p>
  <p class="maxim maxim--complain">Never complain, never explain.</p>
</main>
</body>
</html>
```